The Corbel Ridge Group's website for high impact furniture promotions

I am looking for a simple website. we are a promotional company that runs events for furniture stores to increase sales for short periods of time. i would like the website to have about 4 areas to explain our company. I would like it to be simple and user friendly. I would like a link to chatterbook and a contact section. I am attaching our logo that i would like somewhere large or possibly in the backround. I am open to different color schemes. I would like to convey fast paced, modern, reliable. I am open to all different styles and look forward to seeing whats out there. we are looking for a quick turn around, so if we see one that we like quick, we will pick that one thanks
Reason: looking for some really creative designs and want to give a fair amount of time to produce
Target Market(s)
Retail Furniture store owners
Industry/Entity Type
It Company
Number of Pages Required
1 page
Colors
Look and feel

```html
<!DOCTYPE html>
<html lang="en">
<head>
<meta charset="utf-8">
<title>The Corbel Ridge Group — Furniture Promotions</title>
<link rel="stylesheet" href="https://fonts.googleapis.com/css2?family=Montserrat:wght@600;700&family=Open+Sans:wght@400;600;700&display=swap">
<style>
:root{
  --brown:#8b5a2e;
  --brown-dark:#3a2210;
  --brown-deep:#2a170a;
  --ink:#333333;
  --muted:#555555;
  --grey-band:#ebebeb;
  --footer:#1c1e20;
  --footer-text:#d8d8d8;
  --white:#ffffff;
}
*{margin:0;padding:0;box-sizing:border-box}
html,body{width:1200px;height:3232px;overflow:hidden}
body{position:relative;background:var(--white);font-family:"Open Sans",Arial,sans-serif;color:var(--ink)}
.abs{position:absolute}
.heading{font-family:"Montserrat",Arial,sans-serif;font-weight:700;text-transform:uppercase;color:var(--brown);text-align:center;font-size:28px;letter-spacing:.5px}
.rule{width:120px;height:2px;background:var(--brown);margin:0 auto}

/* nav */
.topline{top:0;left:0;width:1200px;height:4px;background:var(--brown);z-index:5}
.nav{top:0;left:0;width:1200px;height:82px;background:var(--white);z-index:4;box-shadow:0 2px 6px rgba(0,0,0,.15)}
.nav a{position:absolute;top:32px;font-size:17px;font-weight:600;color:#222;text-decoration:none;text-transform:uppercase}
.brand-tab{top:0;left:492px;width:216px;height:162px;border-radius:0 0 108px 108px;background:var(--white);z-index:5;display:flex;flex-direction:column;align-items:center;justify-content:center;padding-top:14px}
.brand-mark{width:48px;height:48px;border-radius:50%;background:var(--brown);margin-bottom:8px}
.brand-name{font-family:"Open Sans",Arial,sans-serif;font-weight:600;font-size:15px;color:var(--brown);text-transform:uppercase;letter-spacing:1.5px;text-align:center;line-height:1.25}

/* hero */
.hero{top:82px;left:0;width:1200px;height:545px;background:linear-gradient(160deg,#6b6250 0%,#4b4234 40%,#2f2820 100%);clip-path:polygon(0 0,100% 0,100% 88%,52% 100%,0 88%)}
.hero-title{top:238px;left:0;width:1200px;text-align:center;font-family:"Montserrat",Arial,sans-serif;font-weight:700;font-size:48px;color:var(--white)}
.hero-sub{top:322px;left:250px;width:700px;text-align:center;font-size:19px;font-weight:600;color:var(--white);line-height:32px}
.btn-more{top:414px;left:534px;width:132px;height:51px;background:#a4774e;border:2px solid #e8d8c4;color:var(--white);font-weight:700;font-size:16px;text-transform:uppercase;display:flex;align-items:center;justify-content:center}
.dots{top:575px;left:546px;display:flex;gap:6px}
.dots span{width:16px;height:16px;border-radius:50%;background:#bdbdbd}
.dots span:first-child{background:#c9a57a}

/* why */
.why{top:692px;left:0;width:1200px}
.why .rule{margin-top:22px}
.why p{width:940px;margin:40px auto 0;text-align:center;font-size:14px;line-height:26px;color:var(--muted)}
.card{top:896px;width:282px;height:280px;background:var(--white);border:1px solid #e3e3e3;box-shadow:0 1px 6px rgba(0,0,0,.12);text-align:center;padding:36px 26px 0}
.card.active{background:var(--brown);border-color:var(--brown)}
.card-icon{width:76px;height:70px;margin:0 auto 26px;display:block}
.card h3{font-family:"Open Sans",Arial,sans-serif;font-weight:700;font-size:19px;color:var(--brown);margin-bottom:14px}
.card p{font-size:13px;line-height:22px;color:var(--muted)}
.card.active h3,.card.active p{color:var(--white)}

/* trading */
.trading{top:1236px;left:0;width:1200px;height:610px;background:linear-gradient(180deg,#4a2c14 0%,#3a2210 50%,#2d190a 100%);clip-path:polygon(0 0,50% 5%,100% 0,100% 100%,50% 95%,0 100%)}
.trading-head{top:1356px;left:0;width:1200px}
.trading-head .heading{color:var(--white)}
.trading-head .rule{background:var(--white);width:80px;margin-top:22px}
.trading-lead{top:1450px;left:120px;width:960px;text-align:center;font-size:16px;line-height:30px;color:#f0e6dc}
.trading-box{top:1551px;left:97px;width:1004px;height:162px;background:rgba(120,86,56,.55);display:flex;align-items:center;padding:0 30px;text-align:center;font-size:13.5px;font-weight:600;line-height:29px;color:#f5ede4}

/* about */
.about-photo{top:1896px;left:118px;width:292px;height:334px;background:linear-gradient(180deg,#f4f1ee 0%,#e4ddd6 100%);border-radius:2px}
.about{top:1890px;left:504px;width:600px}
.about h2{font-family:"Montserrat",Arial,sans-serif;font-weight:700;font-size:28px;color:var(--brown);text-transform:uppercase}
.about .rule{margin:14px 0 0;width:70px}
.about p{margin-top:24px;font-size:14px;line-height:22px;color:var(--muted)}
.about ul{list-style:none;margin-top:14px}
.about li{display:flex;align-items:center;height:36px;font-size:14.5px;font-weight:600;color:#222}
.about li svg{width:22px;height:22px;margin-right:12px;flex:none}

/* faq */
.faq-band{top:2297px;left:0;width:1200px;height:460px;background:var(--grey-band)}
.faq-head{top:2352px;left:0;width:1200px}
.faq-head .rule{margin-top:20px;width:80px}
.faq-item{left:99px;width:476px;height:48px;border:2px solid var(--brown);border-radius:24px;display:flex;align-items:center;justify-content:space-between;padding:0 20px;font-size:15px;font-weight:600;color:var(--brown)}
.faq-item.open{background:var(--brown);color:var(--white);border-radius:24px 0 0 24px;clip-path:polygon(0 0,94% 0,100% 50%,94% 100%,0 100%);width:490px}
.answers{top:2452px;left:623px;width:480px}
.answers h4{font-size:21px;font-weight:600;color:var(--brown);margin-bottom:18px}
.answers li{list-style:none;display:flex;align-items:center;font-size:15px;color:var(--brown);height:30px}
.answers li::before{content:"";width:9px;height:9px;border:2px solid var(--brown);border-radius:50%;margin-right:12px}
.answers p{margin-top:20px;font-size:13.5px;line-height:23px;color:var(--muted)}

/* footer */
.footer{top:2720px;left:0;width:1200px;height:512px;background:var(--footer);clip-path:polygon(0 0,50% 6%,100% 0,100% 100%,0 100%)}
.foot-brand{top:2930px;left:100px;width:210px;display:flex;flex-direction:column;align-items:center}
.foot-brand .brand-mark{width:66px;height:66px;background:#a4774e}
.foot-brand .brand-name{color:#a4774e;font-size:17px}
.foot-col h5{font-family:"Open Sans",Arial,sans-serif;font-weight:700;font-size:16px;color:var(--white);text-transform:uppercase;margin-bottom:12px}
.foot-col .rule{margin:0 0 18px;width:50px;background:var(--white)}
.links li{list-style:none;font-size:14px;color:var(--footer-text);height:32px}
.links li::before{content:"›";margin-right:6px}
.contact-row{display:flex;margin-bottom:20px}
.contact-row .ico{width:40px;height:40px;border:2px solid var(--white);border-radius:50%;flex:none;margin-right:16px;display:flex;align-items:center;justify-content:center}
.contact-row b{display:block;font-size:14px;color:var(--white);text-transform:uppercase;margin-bottom:4px}
.contact-row span{font-size:12px;color:var(--footer-text);line-height:18px}
.form-field{position:absolute;border:1px solid #bdbdbd;border-radius:2px;font-size:11px;color:var(--white);padding:6px 8px}
.send{position:absolute;top:168px;left:0;width:120px;height:38px;background:#a4774e;border:2px solid #e8d8c4;color:var(--white);font-size:12px;font-weight:600;text-transform:uppercase;display:flex;align-items:center;justify-content:center}
.foot-line{top:3146px;left:97px;width:1004px;height:1px;background:#5a5a5a}
.copyright{top:3175px;left:97px;font-size:13px;font-weight:600;color:var(--white)}
.social{top:3166px;left:980px;display:flex;align-items:center;gap:10px;font-size:14px;color:var(--white)}
.social span.ring{width:32px;height:32px;border:2px solid var(--white);border-radius:50%}
</style>
</head>
<body>

<div class="abs topline"></div>
<nav class="abs nav">
  <a style="left:97px">Home</a>
  <a style="left:220px">About Us</a>
  <a style="left:377px">Trading</a>
  <a style="left:750px">Stores</a>
  <a style="left:870px">Furniture</a>
  <a style="left:1022px">Contact</a>
</nav>
<div class="abs brand-tab">
  <span class="brand-mark"></span>
  <span class="brand-name">The Corbel Ridge<br>Group</span>
</div>

<section class="abs hero" role="img" aria-label="Photo of a bright furnished living room with sofas and a coffee table, darkened"></section>
<h1 class="abs hero-title">CORBEL RIDGE GROUP</h1>
<p class="abs hero-sub">We are a promotional company that runs events for furniture stores to increase sales for short periods of time.</p>
<div class="abs btn-more">Read More</div>
<div class="abs dots"><span></span><span></span><span></span><span></span><span></span></div>

<section class="abs why">
  <h2 class="heading">Why Corbel Ridge Group</h2>
  <div class="rule"></div>
  <p>Duis aute irure dolor in reprehenderit in voluptate velit esse cillum dolore eu fugiat nulla pariatur. Excepteur sint occaecat cupidatat non proident, sunt in culpa qui officiar.</p>
</section>

<div class="abs card" style="left:123px">
  <svg class="card-icon" viewBox="0 0 76 70" role="img" aria-label="Promotion icon"><rect x="8" y="12" width="60" height="46" rx="8" fill="#8b5a2e"/></svg>
  <h3>Promotional Company</h3>
  <p>Nemo enim ipsam voluptatem quia voluptas sit aspernatur aut odit aut fugit, sed quia consequuntur.</p>
</div>
<div class="abs card active" style="left:459px">
  <svg class="card-icon" viewBox="0 0 76 70" role="img" aria-label="Trading chart icon"><rect x="10" y="8" width="56" height="44" rx="3" fill="none" stroke="#fff" stroke-width="4"/><polyline points="18,42 30,30 40,36 56,18" fill="none" stroke="#fff" stroke-width="4"/><line x1="38" y1="52" x2="38" y2="64" stroke="#fff" stroke-width="4"/></svg>
  <h3>Trading Services</h3>
  <p>Nemo enim ipsam voluptatem quia voluptas sit aspernatur aut odit aut fugit, sed quia consequuntur.</p>
</div>
<div class="abs card" style="left:795px">
  <svg class="card-icon" viewBox="0 0 76 70" role="img" aria-label="Furniture icon"><rect x="18" y="8" width="40" height="50" rx="8" fill="#8b5a2e"/></svg>
  <h3>Furniture Stores</h3>
  <p>Nemo enim ipsam voluptatem quia voluptas sit aspernatur aut odit aut fugit, sed quia consequuntur.</p>
</div>

<section class="abs trading" role="img" aria-label="Photo of a dim furniture showroom with curtains, tinted brown"></section>
<div class="abs trading-head">
  <h2 class="heading">Our Trading</h2>
  <div class="rule"></div>
</div>
<p class="abs trading-lead">Nemo enim ipsam voluptatem quia voluptas sit aspernatur aut odit aut fugit, sed quia consequuntur magni dolores eos qui ratione voluptatem sequi nesciunt.</p>
<div class="abs trading-box">Sed ut perspiciatis unde omnis iste natus error sit voluptatem accusantium doloremque laudantium, totam rem aperiam, eaque ipsa quae ab illo inventore veritatis et quasi architecto beatae vitae dicta sunt explicabo. Nemo enim ipsam voluptatem quia voluptas sit aspernatur aut odit aut fugit, sed quia consequuntur magni dolores eos qui ratione voluptatem.</div>

<div class="abs about-photo" role="img" aria-label="Photo of an upholstered brown armless chair with wooden legs"></div>
<section class="abs about">
  <h2>About Us</h2>
  <div class="rule"></div>
  <p>Nemo enim ipsam voluptatem quia voluptas sit aspernatur aut odit aut fugit, sed quia consequuntur magni dolores eos qui ratione voluptatem</p>
  <ul>
    <li><svg viewBox="0 0 22 22"><rect x="2" y="4" width="16" height="16" fill="none" stroke="#8b5a2e" stroke-width="2"/><polyline points="6,11 10,15 20,3" fill="none" stroke="#8b5a2e" stroke-width="3"/></svg>Nemo enim ipsam voluptatem quia voluptas</li>
    <li><svg viewBox="0 0 22 22"><rect x="2" y="4" width="16" height="16" fill="none" stroke="#8b5a2e" stroke-width="2"/><polyline points="6,11 10,15 20,3" fill="none" stroke="#8b5a2e" stroke-width="3"/></svg>Aspernatur aut odit aut fugit, sed quia consequuntur</li>
    <li><svg viewBox="0 0 22 22"><rect x="2" y="4" width="16" height="16" fill="none" stroke="#8b5a2e" stroke-width="2"/><polyline points="6,11 10,15 20,3" fill="none" stroke="#8b5a2e" stroke-width="3"/></svg>Neque porro quisquam est, qui dolorem ipsum quia dolor sit amet</li>
    <li><svg viewBox="0 0 22 22"><rect x="2" y="4" width="16" height="16" fill="none" stroke="#8b5a2e" stroke-width="2"/><polyline points="6,11 10,15 20,3" fill="none" stroke="#8b5a2e" stroke-width="3"/></svg>Adipisci velit, sed quia non numquam eius modi tempora</li>
    <li><svg viewBox="0 0 22 22"><rect x="2" y="4" width="16" height="16" fill="none" stroke="#8b5a2e" stroke-width="2"/><polyline points="6,11 10,15 20,3" fill="none" stroke="#8b5a2e" stroke-width="3"/></svg>Enim ad minima veniam, quis nostrum exercitationem ullam</li>
    <li><svg viewBox="0 0 22 22"><rect x="2" y="4" width="16" height="16" fill="none" stroke="#8b5a2e" stroke-width="2"/><polyline points="6,11 10,15 20,3" fill="none" stroke="#8b5a2e" stroke-width="3"/></svg>Quis autem vel eum iure reprehenderit qui in ea voluptate</li>
  </ul>
</section>

<div class="abs faq-band"></div>
<div class="abs faq-head">
  <h2 class="heading">Our FAQ's</h2>
  <div class="rule"></div>
</div>
<div class="abs faq-item open" style="top:2448px">Nemo enim ipsam voluptatem quia?<span style="margin-right:22px">»</span></div>
<div class="abs faq-item" style="top:2508px">Dolores eos qui ratione voluptatem sequi?<span>»</span></div>
<div class="abs faq-item" style="top:2569px">Architecto beatae vitae dicta sunt explicabo?<span>»</span></div>
<div class="abs faq-item" style="top:2629px">Perspiciatis unde omnis iste natus error sit?<span>»</span></div>
<div class="abs answers">
  <h4>Answers to your questions:</h4>
  <ul>
    <li>Nemo enim ipsam voluptatem quia voluptas</li>
    <li>Sed quia non numquam eius modi tempora incidunt</li>
  </ul>
  <p>Sed ut perspiciatis unde omnis iste natus error sit voluptatem accusantium do loremque laudantium, totam rem aperiam.</p>
</div>

<footer class="abs footer"></footer>
<div class="abs foot-brand">
  <span class="brand-mark"></span>
  <span class="brand-name">The Corbel Ridge<br>Group</span>
</div>
<div class="abs foot-col" style="top:2860px;left:340px">
  <h5>Quick Links</h5>
  <div class="rule"></div>
  <ul class="links">
    <li>Home</li><li>About Us</li><li>Trading</li><li>Stores</li><li>Furniture</li><li>Contact Us</li>
  </ul>
</div>
<div class="abs foot-col" style="top:2860px;left:524px;width:250px">
  <h5>Contact Us</h5>
  <div class="rule"></div>
  <div class="contact-row"><div class="ico"><svg width="16" height="20" viewBox="0 0 16 20"><path d="M8 1a6 6 0 0 1 6 6c0 5-6 12-6 12S2 12 2 7a6 6 0 0 1 6-6z" fill="#fff"/><circle cx="8" cy="7" r="2.2" fill="#1c1e20"/></svg></div><div><b>Address,</b><span>Suite 41, Harwell Yard,<br>Elmstead, UK</span></div></div>
  <div class="contact-row"><div class="ico"><svg width="12" height="18" viewBox="0 0 12 18"><rect x="1" y="1" width="10" height="16" rx="2" fill="none" stroke="#fff" stroke-width="2"/><circle cx="6" cy="14" r="1" fill="#fff"/></svg></div><div><b>Phone:</b><span>140 077 3918</span></div></div>
  <div class="contact-row"><div class="ico"><svg width="18" height="14" viewBox="0 0 18 14"><rect x="1" y="1" width="16" height="12" fill="#fff"/><polyline points="1,1 9,8 17,1" fill="none" stroke="#1c1e20" stroke-width="1.5"/></svg></div><div><b style="text-transform:none">Mail:</b><span>hello@corbelridge.example</span></div></div>
</div>
<div class="abs foot-col" style="top:2860px;left:812px;width:290px;height:260px">
  <h5>Contact Form</h5>
  <div class="rule"></div>
  <div class="form-field" style="top:68px;left:0;width:140px;height:36px">Name</div>
  <div class="form-field" style="top:68px;left:150px;width:140px;height:36px">Phone</div>
  <div class="form-field" style="top:112px;left:0;width:290px;height:68px">Message</div>
  <div class="send" style="top:198px">Send Message</div>
</div>
<div class="abs foot-line"></div>
<p class="abs copyright">Copyright © 2017 Corbel Ridge Group. All Right Reserved</p>
<div class="abs social"><span class="ring"></span>chatterbook</div>

</body>
</html>
```